Business Card for Professional Photographer

I'm looking for an eye catching modern clean design that compliments my logo/ website fonts & colours.
I specialise in architecture, corporate & commercial photography so I'm marketing to professional clients rather than portrait / wedding clients.

I would prefer to not have a solid black design.

My logo brand guide is as follows :

Main front font. : Reislust
Main font colour : #fff
Slogan front font : Ubuntu Bold
Monogram front font : Venti Medium
Container colour : #fff

I need print ready files in pdf .png & .eps formats.

Included in the files below are some screen grabs as reference to font & colours etc.

```html
<!DOCTYPE html>
<html lang="en">
<head>
<meta charset="utf-8">
<title>Quiet Aperture – Business Card</title>
<link rel="stylesheet" href="https://fonts.googleapis.com/css2?family=Ubuntu:wght@300;400;500;700&display=swap">
<style>
  :root {
    --backdrop: #25282d;
    --card-dark: #3a3b3d;
    --gold: #d3a047;
    --gold-light: #f4dc8a;
    --gold-deep: #b07a2c;
    --text-light: #eeeeee;
    --white: #ffffff;
  }
  * { margin: 0; padding: 0; box-sizing: border-box; }
  html, body {
    width: 1200px; height: 900px; overflow: hidden;
    background: var(--backdrop);
    font-family: "Ubuntu", sans-serif;
  }
  .canvas {
    position: relative; width: 1200px; height: 900px;
    display: flex; align-items: center; justify-content: center; gap: 60px;
  }
  .card {
    position: relative; width: 520px; height: 318px;
    overflow: hidden; box-shadow: 0 14px 30px rgba(0,0,0,.45);
  }

  /* Back side: contact details */
  .card-back { background: var(--card-dark); color: var(--text-light); }
  .card-back .gold-edge {
    position: absolute; left: 0; right: 0; bottom: 0; height: 6px;
    background: linear-gradient(90deg, var(--gold-deep), var(--gold-light) 45%, var(--gold) 70%, var(--gold-light));
  }
  .brand-block {
    position: absolute; left: 40px; top: 72px; width: 190px; text-align: center;
  }
  .brand-mark-dot {
    width: 44px; height: 44px; border-radius: 50%;
    border: 2px solid var(--gold); margin: 0 auto 14px;
  }
  .brand-name {
    font-weight: 400; font-size: 19px; letter-spacing: 3px;
    color: var(--gold); text-transform: uppercase; white-space: nowrap;
  }
  .brand-tagline {
    margin-top: 5px; font-size: 7px; letter-spacing: 1.6px; color: var(--gold);
  }
  .divider {
    position: absolute; left: 250px; top: 72px; width: 1px; height: 120px;
    background: rgba(255,255,255,.35);
  }
  .contact-block { position: absolute; left: 272px; top: 70px; }
  .person-name {
    font-weight: 700; font-size: 21px; color: var(--gold);
    letter-spacing: .5px; text-transform: uppercase;
  }
  .person-role { font-size: 15px; color: var(--gold); margin-top: 2px; }
  .contact-list { list-style: none; margin-top: 10px; }
  .contact-list li {
    display: flex; align-items: center; gap: 8px;
    font-size: 15px; line-height: 24px; color: var(--text-light);
  }
  .contact-list svg { width: 13px; height: 13px; flex: none; }
  .address {
    position: absolute; left: 40px; bottom: 28px;
    font-size: 15px; color: var(--text-light);
  }

  /* Front side: brand */
  .card-front { color: var(--white); }
  .front-surface {
    position: absolute; inset: 0;
    background: radial-gradient(ellipse at 45% 40%, #f3e191 0%, #dcae52 40%, #c98f38 80%, #b87d2e 100%);
  }
  .front-brand {
    position: absolute; left: 190px; top: 130px; display: flex; align-items: center; gap: 14px;
  }
  .front-brand .brand-mark-dot {
    border-color: var(--white); margin: 0; width: 52px; height: 52px;
  }
  .front-brand .brand-name { color: var(--white); font-size: 22px; }
  .front-brand .brand-tagline { color: var(--white); font-size: 8px; }
</style>
</head>
<body>
<main class="canvas">

  <section class="card card-back" aria-label="Business card back">
    <div class="brand-block">
      <div class="brand-mark-dot"></div>
      <div class="brand-name">Quiet Aperture</div>
      <div class="brand-tagline">Architecture Corporate Commercial</div>
    </div>
    <div class="divider"></div>
    <div class="contact-block">
      <div class="person-name">Marcus Hale</div>
      <div class="person-role">Photographer</div>
      <ul class="contact-list">
        <li>
          <svg viewBox="0 0 14 14" fill="none" stroke="#d3a047" stroke-width="1.4"><circle cx="7" cy="7" r="6"/><path d="M4.5 4.2c.3 2.5 2.4 4.8 5 5.3l.8-1.2-1.4-.8-.7.6c-.9-.4-1.7-1.2-2-2l.6-.7-.8-1.4z" fill="#d3a047" stroke="none"/></svg>
          0400 555 018
        </li>
        <li>
          <svg viewBox="0 0 14 14" fill="none" stroke="#d3a047" stroke-width="1.4"><rect x="1" y="3" width="12" height="8"/><path d="M1 3l6 5 6-5"/></svg>
          info@quietaperture.com.au
        </li>
        <li>
          <svg viewBox="0 0 14 14" fill="none" stroke="#d3a047" stroke-width="1.2"><circle cx="7" cy="7" r="6"/><ellipse cx="7" cy="7" rx="2.6" ry="6"/><path d="M1 7h12"/></svg>
          www.quietaperture.com.au
        </li>
      </ul>
    </div>
    <div class="address">Northern Ridge, Australia</div>
    <div class="gold-edge"></div>
  </section>

  <section class="card card-front" aria-label="Business card front">
    <div class="front-surface" role="img" aria-label="Gold foil surface with a faint repeating circle pattern"></div>
    <div class="front-brand">
      <div class="brand-mark-dot"></div>
      <div>
        <div class="brand-name">Quiet Aperture</div>
        <div class="brand-tagline">Architecture Corporate Commercial</div>
      </div>
    </div>
  </section>

</main>
</body>
</html>
```